VMR business card

Need a business card for a company that provides instructional design and elearning development services. The website is here: http://vantmoro.studio/

I'm attaching a current logo, as well as the old business card design. While I like to keep it clean, the old design is too simplistic for my liking. The only idea I want to reuse from the old design is placing industry jargon on the back of the card, just need a better way to present it. But if you have other ideas for the back--feel free to experiment.

Please use the colors complementary to the color we have on the website. Thank you!

```html
<!DOCTYPE html>
<html lang="en">
<head>
<meta charset="utf-8">
<title>VMR business card</title>
<link rel="stylesheet" href="https://fonts.googleapis.com/css2?family=Fredoka:wght@500;600&family=PT+Sans:wght@400&display=swap">
<style>
  :root {
    --bg: #c9c9c9;
    --teal: #1f9890;
    --teal-light: #3ab8b0;
    --gold: #cfc08c;
    --ink: #3f3f3f;
    --paper: #ffffff;
    --paper-shade: #dedede;
    --white: #ffffff;
  }
  * { box-sizing: border-box; margin: 0; padding: 0; }
  html, body { width: 1200px; height: 900px; overflow: hidden; }
  body {
    background: var(--bg);
    font-family: "PT Sans", sans-serif;
    position: relative;
  }
  .card {
    position: absolute;
    width: 560px;
    height: 320px;
    overflow: hidden;
    box-shadow: 0 6px 14px rgba(0,0,0,0.25);
  }
  .card-front {
    left: 150px; top: 120px;
    background: linear-gradient(90deg, var(--paper) 0%, var(--paper-shade) 100%);
  }
  .card-back {
    left: 490px; top: 470px;
    background: linear-gradient(90deg, var(--teal-light) 0%, var(--teal) 100%);
  }
  .wave { position: absolute; inset: 0; }

  .brand {
    position: absolute;
    display: flex;
    align-items: center;
    gap: 14px;
  }
  .brand-square { width: 46px; height: 46px; }
  .brand-name {
    font-family: "Fredoka", sans-serif;
    font-weight: 600;
    font-size: 52px;
    line-height: 1;
    letter-spacing: 1px;
  }
  .card-front .brand { left: 38px; top: 38px; }
  .card-front .brand-square { background: var(--teal); }
  .card-front .brand-name { color: var(--gold); }
  .card-back .brand { left: 48px; top: 60px; }
  .card-back .brand-square { background: var(--white); }
  .card-back .brand-name { color: var(--white); }

  .holder-name {
    position: absolute;
    left: 55px; top: 178px;
    font-family: "Fredoka", sans-serif;
    font-weight: 600;
    font-size: 27px;
    transform: rotate(-3deg);
    transform-origin: left center;
  }
  .holder-first { color: var(--teal); }
  .holder-last { color: var(--gold); }

  .contact {
    position: absolute;
    right: 26px; top: 200px;
    list-style: none;
    text-align: right;
    color: var(--white);
    font-size: 15px;
    letter-spacing: 0.5px;
  }
  .contact li {
    display: flex;
    justify-content: flex-end;
    align-items: center;
    gap: 8px;
    height: 24px;
  }
  .contact svg { width: 16px; height: 16px; flex: none; }

  .jargon {
    position: absolute;
    left: 300px; top: 48px;
    width: 225px;
    color: var(--white);
    font-size: 14px;
    letter-spacing: 1px;
    line-height: 24px;
  }
  .jargon p { text-align: justify; text-align-last: justify; }
  .jargon .tagline {
    color: var(--gold);
    font-size: 19px;
    letter-spacing: 0.5px;
    margin: 4px 0 6px;
  }
  .edge-tab {
    position: absolute;
    right: 0; top: 222px;
    width: 10px; height: 22px;
    background: var(--gold);
  }
</style>
</head>
<body>

  <section class="card card-front" aria-label="Business card front">
    <svg class="wave" viewBox="0 0 560 320" aria-hidden="true">
      <path d="M0,258 C110,300 240,292 320,222 S470,128 560,126 L560,320 L0,320 Z" fill="var(--gold)"/>
      <path d="M0,272 C112,314 244,304 324,234 S472,142 560,140 L560,320 L0,320 Z" fill="#4a4a4a"/>
      <path d="M0,276 C114,318 246,306 326,236 S474,146 560,144 L560,320 L0,320 Z" fill="var(--teal)"/>
    </svg>

    <div class="brand">
      <span class="brand-square"></span>
      <span class="brand-name">VMR</span>
    </div>

    <p class="holder-name"><span class="holder-first">Dorian</span> <span class="holder-last">Vasquell</span></p>

    <ul class="contact">
      <li>555-014-2738
        <svg viewBox="0 0 16 16" aria-hidden="true"><path d="M3,6 C3,4 5,3 8,3 S13,4 13,6 L11,7 L10,5.5 L6,5.5 L5,7 Z M4,8 L12,8 L13,13 L3,13 Z" fill="var(--gold)"/></svg>
      </li>
      <li>dvasquell@vantmoro.studio
        <svg viewBox="0 0 16 16" aria-hidden="true"><rect x="1" y="3" width="14" height="10" fill="var(--gold)"/><path d="M1,3 L8,9 L15,3" fill="none" stroke="var(--teal)" stroke-width="1.3"/></svg>
      </li>
      <li>www.vantmoro.studio
        <svg viewBox="0 0 16 16" aria-hidden="true"><circle cx="8" cy="8" r="6.5" fill="var(--gold)"/><g fill="none" stroke="var(--teal)" stroke-width="1"><ellipse cx="8" cy="8" rx="3" ry="6.5"/><path d="M1.5,8 H14.5 M2.5,5 H13.5 M2.5,11 H13.5"/></g></svg>
      </li>
    </ul>
  </section>

  <section class="card card-back" aria-label="Business card back">
    <div class="brand">
      <span class="brand-square"></span>
      <span class="brand-name">VMR</span>
    </div>

    <div class="jargon">
      <p>MOBILE LEARNING SCORM</p>
      <p>INSTRUCTIONAL DESIGN LMS</p>
      <p>MOOCS ELEARNING HTML5</p>
      <p class="tagline">HOW CAN WE HELP?</p>
      <p>ADULT LEARNING THEORY</p>
      <p>GAMIFICATION CLASSROOM</p>
      <p>XAPI BLENDED LEARNING</p>
    </div>

    <span class="edge-tab"></span>
  </section>

</body>
</html>
```